Label for Whiskey and Rum Bottle

We are a distillery. Whiskey and Rum We like to have a new label for our bottles. The whiskey bottles are in a wooden case. http://www.korntropfen-muster.ch/store/product/tannwalder-oberkamm-single-malt-whiskey-nr-6 The Rum Bottles have no package. The label is even more important. http://www.korntropfen-muster.ch/store/product/tannwalder-oberkämmer-rum You can see the form of the bottles here www.korntropfen-muster.ch/store Whiskey and rum bottles are for a liter (50 cl) The labels can be with a picture or without. We would like to have something completely new. Therefore we don`t like to make much prescriptions concerning the design. We don`t like to give too much information (text) on the label. Just the information required by law. Consumers should understand the labels without long-reading. (The label-text is below) The 2 labels (Whiskey and rum) should look similar. Probably they have a different color or a different picture or .... It should be clear that the 2 products are from the same distillery. We have the intention to change all our existing labels over time. This gives designers the chance for follow-up projects.

Target Market(s)

Adults, liquor lovers

Requirements
Must have
• Information on the label is in German. (See "") Whiskey: - the name of the whiskey is "Tannwald Ridgeside Single Malt Whiskey" - The Whiskey was matured 5 years in a sherry "5 years in the sherry barrel stored" - The Alcohol content is 40% volumes "40% Vol "- The bottle contents 50 cl" 5 dl "- The distillery is" Distillery Brugghofer, Felsmatt, www.korntropfen-muster.ch "- The producer is" Korvix GmbH "Rum: - The name is" Tannwald Ridgesider Rum "- The alcohol content is 37% Volumes "37% Vol" - The bottle contens 50 cl "5 dl" - The distillery is "Distillery Brugghofer, Felsmatt, www.korntropfen-muster.ch" - The producer is "Korvix GmbH"
Nice to have
• Premium looking label Only front label preferred Only necessary text on the label
Should not have
• No special print techniques necessary No special paper form

```html
<!DOCTYPE html>
<html lang="de">
<head>
<meta charset="utf-8">
<title>Tannwalder Oberkamm Single Malt Whiskey – Etikett</title>
<link rel="stylesheet" href="https://fonts.googleapis.com/css2?family=Cinzel:wght@400;600;700;900&family=Montserrat:wght@500;600&display=swap">
<style>
  :root {
    --page: #ffffff;
    --label-dark: #03080d;
    --label-mid: #0b2a44;
    --label-glow: #1a6a99;
    --silver-light: #ffffff;
    --silver-dark: #8c99a6;
    --gold-light: #ffe27a;
    --gold-dark: #b8801c;
    --text-light: #e4ebef;
    --ornament-teal: #17384a;
    --frame-line: #c9d3da;
  }
  * { margin: 0; padding: 0; box-sizing: border-box; }
  html, body { width: 1200px; height: 1169px; overflow: hidden; background: var(--page); }
  .canvas { position: relative; width: 1200px; height: 1169px; }

  .label {
    position: absolute; left: 155px; top: 60px; width: 908px; height: 1067px; overflow: hidden;
    background:
      linear-gradient(125deg, transparent 38%, rgba(40,130,190,.18) 44%, rgba(40,130,190,.18) 58%, transparent 64%),
      radial-gradient(ellipse 60% 55% at 50% 52%, var(--label-glow) 0%, var(--label-mid) 45%, var(--label-dark) 100%);
  }
  .abs { position: absolute; }
  .center-text { position: absolute; left: 0; right: 0; text-align: center; }

  .corner-ornament { position: absolute; width: 150px; height: 170px; background: radial-gradient(circle at 30% 30%, rgba(35,80,105,.55), rgba(23,56,74,0) 75%); }
  .corner-ornament.tl { left: 20px; top: 20px; }
  .corner-ornament.tr { right: 20px; top: 20px; transform: scaleX(-1); }
  .corner-ornament.bl { left: 20px; bottom: 20px; transform: scaleY(-1); }
  .corner-ornament.br { right: 20px; bottom: 20px; transform: scale(-1,-1); }
  .side-vine { position: absolute; top: 200px; width: 30px; height: 660px; background: linear-gradient(var(--ornament-teal), rgba(23,56,74,.3), var(--ornament-teal)); opacity: .45; border-radius: 15px; }
  .side-vine.left { left: 35px; }
  .side-vine.right { right: 35px; }

  .still-illustration { left: 423px; top: 15px; width: 62px; height: 137px; border-radius: 6px 6px 2px 2px; background: linear-gradient(#b5532a, #7a3415 70%, #6d7278 70%); }
  .gold-flourish { height: 50px; border-radius: 50%; background: linear-gradient(90deg, rgba(184,128,28,0), var(--gold-dark) 30%, var(--gold-light) 75%, var(--gold-dark)); opacity: .85; }
  .gold-flourish.top-left { left: 210px; top: 100px; width: 210px; }
  .gold-flourish.top-right { left: 490px; top: 100px; width: 205px; transform: scaleX(-1); }
  .gold-flourish.bottom { left: 115px; top: 860px; width: 680px; height: 62px; background: linear-gradient(90deg, rgba(184,128,28,0), var(--gold-dark) 20%, var(--gold-light) 50%, var(--gold-dark) 80%, rgba(184,128,28,0)); }

  .brand-name { font-family: "Cinzel", serif; font-weight: 400; font-size: 23px; line-height: 27px; letter-spacing: 1.5px; color: var(--text-light); top: 162px; }

  .title-frame { left: 0; top: 0; }
  .product-title {
    font-family: "Cinzel", serif; font-weight: 900; font-size: 72px; line-height: 100px; letter-spacing: 1px;
    top: 252px;
    background: linear-gradient(180deg, var(--silver-light) 20%, var(--silver-dark) 55%, var(--silver-light) 85%);
    -webkit-background-clip: text; background-clip: text; color: transparent;
    text-shadow: none;
  }
  .product-type {
    font-family: "Cinzel", serif; font-weight: 700; font-size: 38px; line-height: 44px; top: 496px;
    background: linear-gradient(180deg, var(--gold-light), var(--gold-dark));
    -webkit-background-clip: text; background-clip: text; color: transparent;
  }

  .wreath-emblem { left: 370px; top: 505px; width: 175px; height: 195px; border-radius: 45% 45% 50% 50%; background: radial-gradient(circle at 50% 60%, rgba(0,0,0,0) 38%, rgba(200,208,214,.35) 40%, rgba(200,208,214,.15) 60%, rgba(0,0,0,0) 70%); }
  .volume-info { font-family: "Montserrat", sans-serif; color: var(--silver-light); }
  .volume-info .abv { top: 618px; font-size: 36px; font-weight: 600; line-height: 44px; }
  .volume-info .rule { left: 414px; top: 662px; width: 86px; height: 1.5px; background: var(--text-light); }
  .volume-info .size { top: 670px; font-size: 25px; font-weight: 500; line-height: 30px; }
  .silver-flourish { left: 285px; top: 724px; width: 340px; height: 12px; border-radius: 50%; background: linear-gradient(90deg, rgba(200,208,214,0), #c8d0d6 40%, #c8d0d6 60%, rgba(200,208,214,0)); opacity: .8; }

  .maturation { font-family: "Cinzel", serif; font-weight: 400; font-size: 25px; line-height: 33px; color: var(--text-light); top: 750px; }
  .distillery-info { font-family: "Cinzel", serif; font-weight: 400; font-size: 21px; line-height: 30px; letter-spacing: 1.5px; color: var(--text-light); top: 940px; }
</style>
</head>
<body>
<div class="canvas">
  <section class="label">
    <div class="corner-ornament tl" role="img" aria-label="Dekoratives Rankenornament"></div>
    <div class="corner-ornament tr" role="img" aria-label="Dekoratives Rankenornament"></div>
    <div class="corner-ornament bl" role="img" aria-label="Dekoratives Rankenornament"></div>
    <div class="corner-ornament br" role="img" aria-label="Dekoratives Rankenornament"></div>
    <div class="side-vine left" role="img" aria-label="Rankenbordüre links"></div>
    <div class="side-vine right" role="img" aria-label="Rankenbordüre rechts"></div>

    <div class="abs gold-flourish top-left" role="img" aria-label="Goldenes Zierornament"></div>
    <div class="abs gold-flourish top-right" role="img" aria-label="Goldenes Zierornament"></div>
    <div class="abs still-illustration" role="img" aria-label="Illustration einer kupfernen Brennblase"></div>

    <p class="center-text brand-name">Brennerei<br>Brugghofer</p>

    <svg class="abs title-frame" width="908" height="1067" aria-hidden="true">
      <g stroke="var(--frame-line)" stroke-width="1.5" fill="none">
        <line x1="160" y1="307" x2="180" y2="307"/>
        <line x1="728" y1="307" x2="752" y2="307"/>
        <line x1="160" y1="307" x2="160" y2="523"/>
        <line x1="752" y1="307" x2="752" y2="523"/>
        <line x1="160" y1="523" x2="248" y2="523"/>
        <line x1="660" y1="523" x2="752" y2="523"/>
      </g>
    </svg>

    <h1 class="center-text product-title">Tannwalder<br>Oberkamm</h1>
    <p class="center-text product-type">Single Malt Whiskey</p>

    <div class="abs wreath-emblem" role="img" aria-label="Lorbeerkranz mit Krone"></div>
    <div class="volume-info">
      <p class="center-text abv">40%</p>
      <div class="abs rule"></div>
      <p class="center-text size">0.5 L</p>
    </div>
    <div class="abs silver-flourish" role="img" aria-label="Silberne Zierlinie"></div>

    <p class="center-text maturation">5 JAHRE IM SHERRY<br>FASS GELAGERT</p>

    <div class="abs gold-flourish bottom" role="img" aria-label="Goldenes Zierornament"></div>

    <p class="center-text distillery-info">BRENNEREI BRUGGHOFER, FELSMATT<br>WWW.KORNTROPFEN-MUSTER.CH</p>
  </section>
</div>
</body>
</html>
```